Social Media Web Design

We require the design of 3 pages for our social media website. We have designed a general layout, which you can see at the link below:

https://files.quorbelvault.net/folder/d/7KpRt204mWzYuLsHbQnEeTgVxA9/edit?usp=sharing

We need you to design the colour scheme, detailed layout and graphics. We will provide you with three basic HTML pages that will contain text and we would like you to return completed .css files. The html files are only to make your job simpler and to provide details. If it is easier for you to build the .css files from scratch then it is not necessary for you to use them. Also, if you would like to edit the html files feel free. We would like you to focus on the creative design component, specifically colours and graphics.

In terms of colours, we would like to avoid red and blue. We would also prefer not to have various shades of black and dark grey. We like strong, simple design colours that are easy on the eye.
**Update on Colour Themes**
Apologies, I feel that I wasn't entirely clear about the colours, specifically red, blue and black. We'd prefer to stay away from the use of red and blue as a major components of the theme. It is already used quite heavily in other social media sites and we're after a distinct look of our own. I didn't mean to suggest that no red or blue can be used in the design.
***

Some websites that we like the look of include:
https://tindelwisp.com - We particularly like the layout and the colour scheme and contrasts. We would however, prefer to avoid blue themes.
www.gorvabent.com
www.plumeradix.com
www.vastirelon.com - The icons, images and style of this site are really good. As stated above, we'd prefer to avoid black though.

There is no need to design a primary website logo, but please design other icons, buttons and graphics.

We would prefer the page to be bold, modern and fun rather than professional. In addition, we like clean, uncluttered designs and designs that emphasize user experience. The Homepage listed is quite empty in terms of content, so you have freedom to be particularly creative on this page.

If you have any further questions please ask, we are very happy to provide any further details or help you might need.
Updates

Thanks in advance.

Target Market(s)

social media users

Industry/Entity Type

Media

Requirements
Must have
• We require css files at the end of the project.
We require the creation of every field in the design document to complete the project.
The spacial layout must replicate the design document.
Should not have
• Flash, Silverlight

```html
<!DOCTYPE html>
<html lang="en">
<head>
<meta charset="utf-8">
<title>Wrenfield – Welcome</title>
<link rel="stylesheet" href="https://fonts.googleapis.com/css2?family=Archivo+Black&family=Source+Sans+3:wght@400;600&family=Arimo:wght@400;700&display=swap">
<style>
  :root {
    --brand-green: #1a7f68;
    --brand-green-light: #23b996;
    --brand-green-dark: #168a6e;
    --logo-grey: #5f6062;
    --ink: #1d1d1d;
    --nav-grey: #555;
    --field-border: #d5d5d5;
    --field-text: #9a9a9a;
    --white: #ffffff;
  }
  * { box-sizing: border-box; margin: 0; padding: 0; }
  html, body { width: 1200px; height: 564px; overflow: hidden; }
  body { position: relative; background: var(--white); font-family: "Arimo", Arial, sans-serif; }

  .site-header {
    position: absolute; inset: 0 0 auto 0; height: 86px; background: var(--white);
    box-shadow: 0 2px 4px rgba(0,0,0,.08); z-index: 2;
  }
  .brand { position: absolute; left: 182px; top: 19px; display: flex; align-items: center; gap: 14px; }
  .brand-dot { width: 48px; height: 48px; border-radius: 50%; background: var(--brand-green); }
  .brand-name { font-family: "Archivo Black", sans-serif; font-size: 33px; color: var(--logo-grey); }
  .top-nav { position: absolute; right: 185px; top: 44px; display: flex; gap: 28px; font-size: 12px; color: var(--nav-grey); }
  .top-nav span::before { content: "●"; font-size: 8px; margin-right: 4px; color: #777; vertical-align: 1px; }

  .hero-photo {
    position: absolute; left: 0; top: 86px; width: 1200px; height: 414px;
    background:
      radial-gradient(ellipse 220px 200px at 330px 150px, rgba(222,166,120,.55), transparent 70%),
      radial-gradient(ellipse 200px 220px at 560px 230px, rgba(150,120,110,.5), transparent 70%),
      radial-gradient(ellipse 220px 240px at 870px 200px, rgba(200,150,110,.55), transparent 70%),
      radial-gradient(ellipse 260px 220px at 470px 330px, rgba(160,160,175,.5), transparent 70%),
      linear-gradient(90deg, #f7f7f7 0%, #e9e6e3 15%, #d9cdc3 45%, #ddd3ca 70%, #eee9e6 88%, #f8f8f8 100%);
  }

  .welcome { position: absolute; left: 189px; top: 206px; }
  .welcome-lead { font-family: "Archivo Black", sans-serif; font-size: 30px; line-height: 1; color: var(--white); }
  .welcome-name { font-family: "Archivo Black", sans-serif; font-size: 60px; line-height: 1; color: var(--brand-green); margin-top: 2px; }
  .intro { position: absolute; left: 197px; top: 304px; width: 495px; font-family: "Source Sans 3", sans-serif;
    font-size: 10px; line-height: 20px; color: var(--ink); }
  .intro p + p { margin-top: 20px; }

  .account { position: absolute; left: 759px; width: 262px; }
  .account h2 { font-family: "Source Sans 3", sans-serif; font-weight: 600; font-size: 23px; color: var(--ink); margin-bottom: 8px; }
  .field { display: block; width: 259px; height: 26px; margin: 0 0 9px 2px; background: var(--white);
    border: 1px solid var(--field-border); border-radius: 3px; padding-left: 11px; font-size: 11px; line-height: 24px; color: var(--field-text); }
  .action { display: block; margin-left: auto; width: 87px; height: 25px; border-radius: 2px; text-align: center;
    font-size: 14px; line-height: 25px; color: var(--white); border: 1px solid var(--brand-green-dark);
    background: linear-gradient(var(--brand-green-light), var(--brand-green-dark)); }
  .login { top: 160px; }
  .signup { top: 305px; }

  .site-footer { position: absolute; left: 0; top: 500px; width: 1200px; height: 64px; background: var(--brand-green); color: var(--white); font-size: 9.5px; }
  .legal { position: absolute; left: 184px; top: 28px; display: flex; gap: 14px; }
  .social { position: absolute; left: 768px; top: 18px; display: flex; align-items: center; gap: 5px; }
  .social-label { text-align: right; line-height: 11px; margin-right: 2px; }
  .social-icon { width: 22px; height: 22px; border-radius: 3px; }
</style>
</head>
<body>
  <header class="site-header">
    <div class="brand"><span class="brand-dot"></span><span class="brand-name">Wrenfield</span></div>
    <nav class="top-nav"><span>Need Help</span><span>Support</span></nav>
  </header>

  <div class="hero-photo" role="img" aria-label="Soft-focus photo of a cheerful group of friends raising their arms"></div>

  <section class="welcome">
    <div class="welcome-lead">Welcome to</div>
    <div class="welcome-name">Wrenfield</div>
  </section>
  <div class="intro">
    <p>Lorem Ipsum is simply dummy text of the printing and typesetting industry. Lorem Ipsum has been the industry's standard dummy text ever since the 1500s, when an unknown printer took a galley of type and scrambled it to make a type specimen book. It has survived not only five centuries, but also the leap into electronic typesetting, remaining essentially unchanged.</p>
    <p>Lorem Ipsum is simply dummy text of the printing and typesetting industry. Lorem Ipsum has been the industry's standard dummy text ever since the 1500s.</p>
  </div>

  <section class="account login">
    <h2>Login</h2>
    <span class="field">Email ID :</span>
    <span class="field">Password :</span>
    <span class="action">Login</span>
  </section>
  <section class="account signup">
    <h2>Sign Up</h2>
    <span class="field">Email ID :</span>
    <span class="field">Password :</span>
    <span class="field">Conform Password :</span>
    <span class="action">Sign Up</span>
  </section>

  <footer class="site-footer">
    <div class="legal">
      <span>Copyright © 2013 Wrenfield. All Rights Reserved.</span><span>|</span>
      <span>Terms &amp; Conditions</span><span>|</span>
      <span>Privacy poloicy</span><span>|</span>
      <span>Security</span>
    </div>
    <div class="social">
      <div class="social-label">Connect to<br>our Social Network :</div>
      <span class="social-icon" style="background:#4a6fa0"></span>
      <span class="social-icon" style="background:#4d8fb8"></span>
      <span class="social-icon" style="background:#5ab0cf"></span>
      <span class="social-icon" style="background:#e0782e"></span>
      <span class="social-icon" style="background:#4f86b5"></span>
      <span class="social-icon" style="background:#c23a33"></span>
    </div>
  </footer>
</body>
</html>
```